Lumora vale- referral cards for new customers

Hey,

I would like 1 set of business cards with the following details:

10% off any sales / coupon code
Our phone number: 4702938165
Menu :Lumoravale.example (for the menu)
A line left blank to hand write an activation code: either on top or just on one side

Include the Lumora Vale logo ( your choice of black or white logo)
This card is to drive orders for people to order a cannabis order with Lumora Vale. Please make the logo a large part of the card on both sides.

Target Market(s)

People who consume cannabis 21 and up

Industry/Entity Type

Business

Contact Information for Business Card

This business card will be given to customers so they can then give it to other customers and generate referalls. We need this card to be elegant, impressionable, professional, and something worth keeping and passing to friends.

Font styles to use
Decorative
Script

Colors
33a6d7
85acd3
3176b5
0455a3
0592cd
85cae6
cee9f5
eaf1f7
757575

Requirements
Must have
• Our website
• Phone Number
• The 10% off an order
• Spot for activation code
Nice to have
• Eye catching design
• Look classy
• Textured feel or textured look
Should not have
• Do not look super cannabis heady
• Do not look attractive to children

```html
<!DOCTYPE html>
<html lang="en">
<head>
<meta charset="utf-8">
<title>Lumora Vale – Referral Cards</title>
<link href="https://fonts.googleapis.com/css2?family=Sorts+Mill+Goudy&display=swap" rel="stylesheet">
<style>
  :root {
    --olive: #6b6c2c;
    --olive-dark: #55561f;
    --cream: #fbf9f0;
    --ink: #1c1c1c;
    --stage: #e8e8e8;
    --art-light: #cfd8d2;
    --art-dark: #4b5a3a;
  }
  * { margin: 0; padding: 0; box-sizing: border-box; }
  html, body { width: 1200px; height: 900px; overflow: hidden; }
  body {
    background: var(--stage);
    font-family: "Sorts Mill Goudy", Georgia, serif;
    color: var(--ink);
    position: relative;
  }
  .card {
    position: absolute;
    top: 290px;
    width: 540px;
    height: 310px;
    border-radius: 22px;
    overflow: hidden;
    box-shadow: 0 6px 18px rgba(0,0,0,0.18);
  }
  .card-front { left: 45px; background: var(--olive); }
  .card-back { left: 615px; background: var(--cream); }

  .cloud-ornament {
    position: absolute;
    left: 40px; top: 18px;
    width: 400px; height: 292px;
    border-radius: 160px 160px 40px 40px;
    background: radial-gradient(ellipse at 50% 45%, #ffffff 60%, #ececec 100%);
  }
  .logo-art {
    position: absolute;
    border-radius: 50%;
    background: radial-gradient(circle at 50% 40%, var(--art-light) 0%, #8ca3a0 45%, var(--art-dark) 100%);
  }
  .card-front .logo-art { left: 165px; top: 55px; width: 150px; height: 150px; }
  .brand-name {
    position: absolute;
    font-size: 30px;
    letter-spacing: 1px;
    color: var(--ink);
    white-space: nowrap;
  }
  .card-front .brand-name { left: 160px; top: 212px; }

  .frame {
    position: absolute;
    inset: 14px;
    border: 6px solid var(--olive);
    border-radius: 14px;
  }
  .card-back .logo-art { left: 82px; top: 70px; width: 160px; height: 160px; }
  .card-back .brand-name { left: 92px; top: 232px; }

  .details {
    position: absolute;
    left: 300px; top: 60px;
    width: 210px;
    text-align: center;
    line-height: 1.15;
  }
  .phone { font-size: 23px; }
  .menu-label {
    display: inline-block;
    margin-top: 8px;
    font-size: 15px;
    color: var(--olive);
    text-decoration: underline;
  }
  .website { font-size: 15px; }
  .find-us { margin-top: 10px; font-size: 13px; }
  .find-us .label { color: var(--olive); margin-right: 4px; }
  .networks {
    display: flex;
    justify-content: center;
    gap: 6px;
    margin-top: 4px;
    font-size: 10px;
    color: var(--olive);
  }
  .networks span::before {
    content: "";
    display: inline-block;
    width: 7px; height: 7px;
    border-radius: 50%;
    background: var(--olive);
    margin-right: 2px;
  }
  .offer { margin-top: 12px; font-size: 17px; }
  .offer .highlight { color: var(--olive); }
  .delivery { font-size: 17px; margin-top: 2px; }
  .coupon-label { margin-top: 4px; font-size: 12px; color: var(--olive); }
  .coupon-field {
    width: 76px; height: 17px;
    margin: 2px auto 0;
    border: 1px solid var(--olive);
  }
</style>
</head>
<body>
  <section class="card card-front">
    <div class="cloud-ornament" role="img" aria-label="White swirling cloud ornament framing the logo"></div>
    <div class="logo-art" role="img" aria-label="Lumora Vale logo illustration"></div>
    <p class="brand-name">Lumora Vale</p>
  </section>

  <section class="card card-back">
    <div class="frame"></div>
    <div class="logo-art" role="img" aria-label="Lumora Vale logo illustration"></div>
    <p class="brand-name">Lumora Vale</p>

    <div class="details">
      <p class="phone">470-293-8165</p>
      <p class="menu-label">Menu</p>
      <p class="website">www.LumoraVale.example</p>
      <p class="find-us"><span class="label">Find us</span>@LumoraValeDelivery</p>
      <div class="networks">
        <span>Circleo</span><span>Chirply</span><span>Snapwise</span><span>Leafmap</span>
      </div>
      <p class="offer"><span class="highlight">10% OFF</span> ANY Order</p>
      <p class="delivery">&amp; Free Delivery</p>
      <p class="coupon-label">coupon code</p>
      <div class="coupon-field"></div>
    </div>
  </section>
</body>
</html>
```